A billboard for Harlow Ridge Construction size 36.5’ x 14.5’

Hi guys. We are purchasing a billboard and are looking for a design (size 36.5’ x 14.5’). Our slogan is "Quality you deserve, service you can count on". The goal of this billboard is brand recognition primarily letting people know we do roofs. Attached are logos that can be used if needed. Not necessarily all of them need to be used.

Target Market(s)

Residents in the local areas needing or thinking about a roof replacement

Industry/Entity Type

Roofing

Requirements
Must have
• Logo and services (roof replacement, gutters, siding, and snow removal)
Nice to have
• take a look at our website for ideas www.harlowridgeconstruction.example

```html
<!DOCTYPE html>
<html lang="en">
<head>
<meta charset="utf-8">
<title>Harlow Ridge Construction Billboard</title>
<link href="https://fonts.googleapis.com/css2?family=Montserrat:wght@700;800;900&family=Playfair+Display:wght@400&display=swap" rel="stylesheet">
<style>
  :root {
    --red: #e3191b;
    --black: #0d0d0d;
    --white: #ffffff;
    --page: #ffffff;
    --sky-top: #5f8fcf;
    --sky-low: #a9c4e4;
    --brick: #8a6a55;
    --shrub: #5d6e3c;
    --badge-blue: #1d5f8c;
    --badge-dark: #3a3a3a;
    --badge-grey: #b9b9b9;
  }
  * { margin: 0; padding: 0; box-sizing: border-box; }
  html, body { width: 1196px; height: 1200px; overflow: hidden; background: var(--page); }
  .billboard {
    position: absolute; left: 48px; top: 382px;
    width: 1100px; height: 437px;
    background: var(--white);
    box-shadow: 0 8px 28px rgba(0,0,0,0.28);
    overflow: hidden;
  }
  .billboard svg.shapes, .billboard svg.house-photo { position: absolute; left: 0; top: 0; }
  .logo {
    position: absolute; left: 100px; top: 66px;
    display: flex; align-items: center; gap: 26px;
  }
  .logo-square { width: 80px; height: 80px; background: var(--black); }
  .logo-name {
    font-family: "Playfair Display", serif; font-weight: 400;
    font-size: 48px; line-height: 54px; color: var(--black);
  }
  .slogan {
    position: absolute; left: 14px; top: 206px;
    font-family: "Montserrat", sans-serif; font-weight: 900;
    font-size: 44px; line-height: 44px; color: var(--red);
    letter-spacing: 0.2px; text-transform: uppercase;
  }
  .services {
    position: absolute; top: 310px;
    font-family: "Montserrat", sans-serif; font-weight: 700;
    font-size: 21px; line-height: 26px; color: var(--black);
    list-style: none;
  }
  .services li { position: relative; padding-left: 18px; }
  .services li::before {
    content: ""; position: absolute; left: 0; top: 9px;
    border-left: 8px solid var(--red);
    border-top: 5px solid transparent; border-bottom: 5px solid transparent;
  }
  .services.col-1 { left: 14px; }
  .services.col-2 { left: 352px; }
  .services.col-3 { left: 541px; }
  .contact-phone {
    position: absolute; left: 10px; top: 385px; height: 52px;
    display: flex; align-items: center; gap: 6px;
    font-family: "Montserrat", sans-serif; font-weight: 800;
    font-size: 42px; color: var(--white);
  }
  .contact-web {
    position: absolute; left: 376px; top: 385px; height: 52px;
    display: flex; align-items: center; gap: 8px;
    font-family: "Montserrat", sans-serif; font-weight: 700;
    font-size: 22px; color: var(--white);
  }
  .contact-web .tld { color: var(--red); }
</style>
</head>
<body>
  <div class="billboard">
    <svg class="house-photo" width="1100" height="437" viewBox="0 0 1100 437" role="img" aria-label="Photo of a brick two-storey house with a new brown shingle roof under a blue sky">
      <defs>
        <linearGradient id="photoTone" x1="0" y1="0" x2="0" y2="1">
          <stop offset="0" stop-color="var(--sky-top)"/>
          <stop offset="0.38" stop-color="var(--sky-low)"/>
          <stop offset="0.55" stop-color="var(--brick)"/>
          <stop offset="1" stop-color="var(--shrub)"/>
        </linearGradient>
      </defs>
      <polygon points="625,0 1100,0 1100,385 844,385" fill="url(#photoTone)"/>
    </svg>

    <svg class="shapes" width="1100" height="437" viewBox="0 0 1100 437" aria-hidden="true">
      <defs>
        <linearGradient id="ruleFade" x1="0" y1="0" x2="1" y2="0">
          <stop offset="0" stop-color="var(--red)" stop-opacity="0"/>
          <stop offset="0.35" stop-color="var(--red)"/>
          <stop offset="1" stop-color="var(--red)" stop-opacity="0"/>
        </linearGradient>
      </defs>
      <rect x="14" y="198" width="700" height="2" fill="url(#ruleFade)"/>
      <rect x="14" y="301" width="790" height="1.5" fill="url(#ruleFade)"/>
      <polygon points="0,385 813,385 834,437 0,437" fill="var(--black)"/>
      <polygon points="0,385 342,385 360,437 0,437" fill="var(--red)"/>
      <rect class="badge" x="850" y="396" width="90" height="32" rx="2" fill="var(--badge-blue)"/>
      <circle class="badge" cx="990" cy="412" r="17" fill="var(--badge-dark)"/>
      <rect class="badge" x="1046" y="400" width="24" height="24" fill="var(--badge-grey)"/>
    </svg>

    <div class="logo">
      <span class="logo-square"></span>
      <span class="logo-name">Harlow Ridge<br>Construction</span>
    </div>

    <h1 class="slogan">Quality you deserve,<br>Service you can count on</h1>

    <ul class="services col-1">
      <li>Residential &amp; Commercial<br>Roof Replacement</li>
    </ul>
    <ul class="services col-2">
      <li>Roof Repairs</li>
      <li>Gutters</li>
    </ul>
    <ul class="services col-3">
      <li>Siding</li>
      <li>Snow Removal</li>
    </ul>

    <div class="contact-phone">
      <svg width="28" height="28" viewBox="0 0 24 24" aria-hidden="true">
        <path d="M6.6 10.8c1.4 2.8 3.8 5.1 6.6 6.6l2.2-2.2c.3-.3.7-.4 1-.2 1.1.4 2.3.6 3.6.6.6 0 1 .4 1 1V20c0 .6-.4 1-1 1C10.6 21 3 13.4 3 4c0-.6.4-1 1-1h3.5c.6 0 1 .4 1 1 0 1.3.2 2.5.6 3.6.1.3 0 .7-.2 1L6.6 10.8z" fill="var(--white)"/>
      </svg>
      <span>262-555-0187</span>
    </div>

    <div class="contact-web">
      <svg width="22" height="22" viewBox="0 0 24 24" aria-hidden="true">
        <g fill="none" stroke="var(--red)" stroke-width="1.8">
          <circle cx="12" cy="12" r="10"/>
          <ellipse cx="12" cy="12" rx="4.5" ry="10"/>
          <line x1="2" y1="12" x2="22" y2="12"/>
          <line x1="4" y1="6.5" x2="20" y2="6.5"/>
          <line x1="4" y1="17.5" x2="20" y2="17.5"/>
        </g>
      </svg>
      <span>Harlowridgeconstruction<span class="tld">.example</span></span>
    </div>
  </div>
</body>
</html>
```